HARLOWE CONSERVATORY SAXOPHONE SENIOR RECITAL

I need a poster design for my senior saxophone recital. The title of it is "Quill: a Voyage beneath the Edge of Tone". My concept is completely contrasting to the idea of a typical university recital. I'm so put off by the idea of "clap..clap..{play some music}..clap..clap..repeat". My recital is all based off of sound. The music I selected is all very modern (i.e Brem Ostrakel 'Warm from the First Pour' for Saxophone and Coffee Machine). I've included the Chatterbox link so you can see the picture I have in the background. I like the idea of minimal black and white photography. Also, I would like the time / date / location / etc. all included on it. Let your imaginations run wild! It's art for an artist!
https://www.chatterbox-example.net/events/412093857716230/
Target Market(s)
University Students around the Harlowe Conservatory and locals around the art district of South Beach, FL.
Industry/Entity Type
University
Look and feel

```html
<!DOCTYPE html>
<html lang="en">
<head>
<meta charset="utf-8">
<title>Quill: a Voyage beneath the Edge of Tone — Senior Saxophone Recital</title>
<link rel="stylesheet" href="https://fonts.googleapis.com/css2?family=Bebas+Neue&family=Libre+Baskerville&display=swap">
<style>
  :root {
    --ink: #000000;
    --paper: #ffffff;
    --sky-light: #d9d9d9;
    --sky-mid: #8a8a8a;
    --sky-dark: #2a2a2a;
    --ground: #111111;
  }
  html, body {
    margin: 0;
    padding: 0;
    width: 960px;
    height: 1200px;
    overflow: hidden;
    background: var(--ink);
  }
  .poster {
    position: relative;
    width: 960px;
    height: 1200px;
    background: var(--ink);
    color: var(--paper);
    font-family: "Bebas Neue", "Oswald", sans-serif;
    overflow: hidden;
  }
  .recital-heading {
    position: absolute;
    top: 70px;
    left: 0;
    width: 960px;
    margin: 0;
    text-align: center;
    font-weight: 400;
    font-size: 33px;
    letter-spacing: 6.2px;
    line-height: 1;
  }
  .backdrop-photo {
    position: absolute;
    left: 40px;
    top: 140px;
    width: 880px;
    height: 840px;
    background:
      radial-gradient(ellipse 50% 50% at 50% 50%, transparent 55%, var(--ink) 100%),
      linear-gradient(to bottom,
        var(--sky-dark) 0%,
        var(--sky-light) 14%,
        var(--sky-mid) 28%,
        var(--sky-dark) 42%,
        var(--ink) 48%,
        var(--ink) 64%,
        #3a3a3a 70%,
        #1e1e1e 80%,
        #6a6a6a 84%,
        var(--ground) 88%,
        var(--ink) 100%);
  }
  .title-band {
    position: absolute;
    left: 0;
    top: 510px;
    width: 960px;
    height: 172px;
    background: var(--ink);
    text-align: center;
  }
  .recital-title {
    margin: 0;
    padding-top: 26px;
    font-weight: 400;
    font-size: 126px;
    letter-spacing: 30px;
    line-height: 0.82;
    text-indent: 30px;
  }
  .recital-subtitle {
    margin: 14px 0 0;
    font-size: 31px;
    letter-spacing: 5.4px;
    line-height: 1;
  }
  .recital-date {
    position: absolute;
    top: 702px;
    left: 0;
    width: 960px;
    text-align: center;
    line-height: 1;
  }
  .date-day {
    display: block;
    font-family: "Libre Baskerville", Georgia, serif;
    font-size: 32px;
  }
  .date-month {
    display: block;
    margin-top: 12px;
    font-size: 32px;
    letter-spacing: 4px;
  }
  .date-year {
    display: block;
    margin-top: 2px;
    font-size: 50px;
    letter-spacing: 5px;
  }
  .recital-venue {
    position: absolute;
    top: 1040px;
    left: 0;
    width: 960px;
    margin: 0;
    text-align: center;
    font-style: normal;
    font-size: 31px;
    letter-spacing: 5.6px;
    line-height: 1.05;
  }
  .venue-line { display: block; }
  .venue-line--hall { padding-left: 20px; }
</style>
</head>
<body>
  <main class="poster">
    <h2 class="recital-heading">Dario Venturelli Senior Saxophone Recital</h2>

    <div class="backdrop-photo" role="img" aria-label="Blurred black and white photograph of dark treetops against a pale sky above, and a dusky horizon with distant lights over an open field below"></div>

    <header class="title-band">
      <h1 class="recital-title">QUILL</h1>
      <p class="recital-subtitle">A Voyage beneath the Edge of Tone</p>
    </header>

    <p class="recital-date">
      <span class="date-day">8</span>
      <span class="date-month">December</span>
      <span class="date-year">2013</span>
    </p>

    <address class="recital-venue">
      <span class="venue-line">Halden E. Marsh</span>
      <span class="venue-line venue-line--hall">Recital Hall</span>
    </address>
  </main>
</body>
</html>
```